Postcard

I'm a realtor looking to create a general postcard for my business to be mailed out to homeowners. I have a good idea of what I'm looking for, just need someone to put it all together and make it look good. Please keep colors similar to the logo. The save money symbol can be different colors to help stand out. File #6 is the theme for the bottom section of file #5.

Realtor

```html
<!DOCTYPE html>
<html lang="en">
<head>
<meta charset="utf-8">
<title>Harlow Realty – Postcard</title>
<link href="https://fonts.googleapis.com/css2?family=Alex+Brush&family=Lato:wght@400;700&family=Oswald:wght@600&family=Tinos&display=swap" rel="stylesheet">
<style>
  :root {
    --brand-blue: #1b4592;
    --deep-blue: #1a3a86;
    --sun-yellow: #f7c411;
    --sun-light: #fbd437;
    --badge-red: #c81f26;
    --paper: #ffffff;
    --stripe-grey: #dcdde2;
    --ink: #1c1c1c;
  }
  * { margin: 0; padding: 0; box-sizing: border-box; }
  html, body { width: 1200px; height: 829px; overflow: hidden; background: #ffffff; }
  .postcard { position: relative; width: 1200px; height: 829px; overflow: hidden; font-family: "Lato", sans-serif; }
  .postcard__backdrop, .postcard__photo { position: absolute; left: 0; top: 0; }

  .brand { position: absolute; left: 0; top: 0; width: 600px; height: 281px; color: var(--paper); text-align: center; font-family: "Lato", sans-serif; font-weight: 400; }
  .brand__name { position: absolute; left: 0; right: 0; top: 58px; font-size: 104px; line-height: 1; }
  .brand__suffix { position: absolute; left: 0; right: 0; top: 176px; font-size: 40px; letter-spacing: 3px; }

  .phone { position: absolute; left: 0; top: 281px; width: 610px; height: 74px; line-height: 74px; text-align: center; font-weight: 700; font-size: 46px; letter-spacing: 4px; color: var(--deep-blue); }

  .badge { position: absolute; left: 588px; top: 48px; width: 160px; height: 160px; border-radius: 50%; background: radial-gradient(circle at 40% 35%, #e2333a, var(--badge-red) 70%); border: 5px solid #ececec; box-shadow: 0 4px 8px rgba(0,0,0,.3); color: var(--paper); display: flex; flex-direction: column; justify-content: center; align-items: center; transform: rotate(-20deg); font-weight: 700; line-height: 1; }
  .badge__top { font-size: 40px; }
  .badge__bottom { font-size: 30px; margin-top: 4px; }

  .offer { position: absolute; right: 54px; top: 28px; text-align: right; font-family: "Alex Brush", cursive; color: var(--ink); line-height: 1; }
  .offer__lead { font-size: 72px; }
  .offer__rate { font-size: 96px; margin-top: -4px; }

  .features__title { position: absolute; left: 688px; top: 226px; font-family: "Oswald", sans-serif; font-weight: 600; font-size: 35px; letter-spacing: .5px; color: var(--brand-blue); text-transform: uppercase; white-space: nowrap; }
  .features__item { position: absolute; font-family: "Tinos", serif; font-size: 24px; color: var(--ink); white-space: nowrap; line-height: 28px; padding-left: 40px; }
  .features__item::before { content: ""; position: absolute; left: 0; top: 8px; width: 13px; height: 13px; border-radius: 50%; background: var(--brand-blue); }

  .website { position: absolute; left: 512px; top: 727px; width: 688px; height: 74px; background: var(--paper); box-shadow: 0 6px 0 rgba(0,0,0,.15); display: flex; align-items: center; justify-content: center; font-weight: 700; font-size: 42px; letter-spacing: 4px; color: var(--brand-blue); }
</style>
</head>
<body>
<main class="postcard">
  <svg class="postcard__backdrop" width="1200" height="829" viewBox="0 0 1200 829" aria-hidden="true">
    <defs>
      <linearGradient id="sunFade" x1="0" y1="0" x2="1" y2="0">
        <stop offset="0" stop-color="var(--sun-light)"/>
        <stop offset="1" stop-color="var(--sun-yellow)"/>
      </linearGradient>
    </defs>
    <rect width="1200" height="829" fill="var(--paper)"/>
    <polygon points="0,0 650,0 576,281 0,281" fill="var(--brand-blue)"/>
    <polygon points="650,0 723,0 503,829 430,829" fill="var(--stripe-grey)"/>
    <polygon points="723,0 1200,0 1200,829 503,829" fill="url(#sunFade)"/>
  </svg>

  <svg class="postcard__photo" width="1200" height="829" viewBox="0 0 1200 829" role="img" aria-label="Photo of a smiling family of four standing in front of their house holding a For Sale sign">
    <defs>
      <linearGradient id="photoTone" x1="0" y1="0" x2="0" y2="1">
        <stop offset="0" stop-color="#d9dde0"/>
        <stop offset=".55" stop-color="#b9bcc0"/>
        <stop offset="1" stop-color="#7d9a5a"/>
      </linearGradient>
    </defs>
    <polygon points="0,355 630,355 505,829 0,829" fill="url(#photoTone)"/>
  </svg>

  <header class="brand">
    <div class="brand__name">Harlow</div>
    <div class="brand__suffix">REALTY, LLC</div>
  </header>
  <div class="phone">555.014.2790</div>

  <div class="badge"><span class="badge__top">SAVE</span><span class="badge__bottom">MONEY</span></div>

  <div class="offer">
    <div class="offer__lead">Unbeatable</div>
    <div class="offer__rate">3.5%</div>
  </div>

  <section class="features">
    <h2 class="features__title">Full Service Listings Include:</h2>
    <div class="features__item" style="left:701px;top:275px">Professional photography</div>
    <div class="features__item" style="left:692px;top:312px">Full color Brochures</div>
    <div class="features__item" style="left:682px;top:349px">Digital Floor Plans</div>
    <div class="features__item" style="left:673px;top:386px">Personilised Website</div>
    <div class="features__item" style="left:664px;top:423px">Featured Listings on HomeFinder &amp; NestView</div>
    <div class="features__item" style="left:654px;top:460px">Full MLS Benefits</div>
    <div class="features__item" style="left:645px;top:497px">Open House</div>
    <div class="features__item" style="left:636px;top:534px">Sign Post in yard</div>
    <div class="features__item" style="left:626px;top:571px">Solar Power Brochure Box</div>
    <div class="features__item" style="left:617px;top:608px">Additional Discount for unrepresented buyers</div>
    <div class="features__item" style="left:608px;top:645px">Expect Negotiations</div>
    <div class="features__item" style="left:598px;top:682px">Much much more!!</div>
  </section>

  <footer class="website">www.harlowrealty.com</footer>
</main>
</body>
</html>
```